Quorvex business card design

create modern and tech looking business card that is clean but effectively communciates that we are a cloud communications company.
Should have at minimum:
Employee Name
Postion
Phone Number
Email
website
create modern and tech looking business card that is clean but effectively communciates that we are a cloud communications company. We have two logo color schemes (attached) so would like to see designs both ways
Should have at minimum:
Employee Name
Postion
Phone Number
Email
website

```html
<!DOCTYPE html>
<html lang="en">
<head>
<meta charset="utf-8">
<title>Quorvex business card</title>
<link rel="stylesheet" href="https://fonts.googleapis.com/css2?family=Open+Sans:wght@400;600;700&display=swap">
<style>
  :root {
    --backdrop: #3a3a3a;
    --card-black: #000000;
    --card-white: #ffffff;
    --brand-blue: #29b6e6;
    --brand-green: #8cc63f;
    --ink-light: #ffffff;
    --ink-dark: #4a4a4a;
  }
  * { margin: 0; padding: 0; box-sizing: border-box; }
  html, body {
    width: 1200px; height: 864px; overflow: hidden;
    background: var(--backdrop);
    font-family: "Open Sans", Arial, sans-serif;
  }
  .stage { position: relative; width: 1200px; height: 864px; }
  .card {
    position: absolute; width: 560px; height: 320px;
    overflow: hidden;
    box-shadow: 0 12px 30px rgba(0,0,0,.45);
  }
  .card--back { left: 110px; top: 100px; background: var(--card-black); }
  .card--front { left: 530px; top: 440px; background: var(--card-white); }

  .brand {
    position: absolute; display: flex; align-items: center; gap: 14px;
    font-weight: 600; letter-spacing: 1px; text-transform: uppercase;
    white-space: nowrap;
  }
  .brand__dot { width: 30px; height: 30px; border-radius: 50%; background: var(--brand-blue); }
  .card--back .brand { left: 50%; top: 118px; transform: translateX(-50%); font-size: 44px; color: var(--ink-light); }
  .card--back .website {
    position: absolute; left: 0; right: 0; bottom: 28px; text-align: center;
    color: var(--ink-light); font-size: 17px; letter-spacing: .5px;
  }

  .front-panel { position: absolute; inset: 0; }
  .card--front .brand { left: 44px; top: 138px; font-size: 32px; color: var(--ink-dark); }
  .card--front .brand__dot { width: 22px; height: 22px; }

  .contact {
    position: absolute; left: 372px; top: 56px; width: 182px;
    color: var(--ink-light); font-size: 12px; line-height: 1.4;
    white-space: nowrap;
  }
  .contact__name { color: var(--brand-blue); font-size: 19px; font-weight: 700; line-height: 1.15; }
  .contact__role { font-size: 12.5px; margin-bottom: 14px; }
  .contact__address { margin-bottom: 12px; }
  .contact__list { list-style: none; }
  .contact__list li { display: flex; align-items: center; gap: 7px; }
  .contact__list svg { width: 11px; height: 11px; flex: none; }
</style>
</head>
<body>
<main class="stage">

  <section class="card card--back" aria-label="Card back">
    <div class="brand"><span class="brand__dot"></span><span>Quorvex</span></div>
    <p class="website">www.quorvexcloud.net</p>
  </section>

  <section class="card card--front" aria-label="Card front">
    <svg class="front-panel" viewBox="0 0 560 320" preserveAspectRatio="none" aria-hidden="true">
      <path d="M294 0 C 294 140, 324 250, 398 320 L 560 320 L 560 0 Z" fill="var(--brand-green)"/>
      <path d="M304 0 C 304 140, 334 250, 410 320 L 560 320 L 560 0 Z" fill="var(--card-black)"/>
    </svg>

    <div class="brand"><span class="brand__dot"></span><span>Quorvex</span></div>

    <div class="contact">
      <p class="contact__name">Dana Keller</p>
      <p class="contact__role">President</p>
      <p class="contact__address">Harbor Line Ave, Suite 210<br>Region, Postcode, Country</p>
      <ul class="contact__list">
        <li><svg viewBox="0 0 12 12"><path d="M2 1 L4 1 L5 4 L3.6 5 Q5 7.6 7 8.4 L8 7 L11 8 L11 10 Q11 11 10 11 Q1 10 1 2 Q1 1 2 1Z" fill="var(--brand-blue)"/></svg>01 555-204-1187</li>
        <li><svg viewBox="0 0 12 12"><rect x="3" y="0.5" width="6" height="11" rx="1" fill="none" stroke="var(--brand-blue)" stroke-width="1.2"/><circle cx="6" cy="9.6" r=".7" fill="var(--brand-blue)"/></svg>01 555-204-1190</li>
        <li><svg viewBox="0 0 12 12"><rect x="0.5" y="2.5" width="11" height="7" fill="none" stroke="var(--brand-blue)" stroke-width="1.2"/><path d="M0.5 2.5 L6 7 L11.5 2.5" fill="none" stroke="var(--brand-blue)" stroke-width="1.2"/></svg>hello@quorvexcloud.net</li>
        <li><svg viewBox="0 0 12 12"><circle cx="6" cy="6" r="5.2" fill="none" stroke="var(--brand-blue)" stroke-width="1.1"/><ellipse cx="6" cy="6" rx="2.3" ry="5.2" fill="none" stroke="var(--brand-blue)" stroke-width="1"/><path d="M1 6 H11" stroke="var(--brand-blue)" stroke-width="1"/></svg>quorvexcloud.net</li>
      </ul>
    </div>
  </section>

</main>
</body>
</html>
```